Mosquito and outdoor pest management

The uploaded logo must be integrated as the main theme of the card. I would like it to be modern and eye catching. Maybe some backround images or light silver metallic background.
Space enough at the base for contact info to be put in- phone numbers,emails,names,website.
Space on the back for short blog and lines for hand writing..calling card.
Commercial- golf courses, schools, outdoor function properties, pre event treatments.
Residential- retirement villages, townhome complexes and general houses
Management

```html
<!DOCTYPE html>
<html lang="en">
<head>
<meta charset="utf-8">
<title>Bayline Mosquito Care – Business Card</title>
<link rel="stylesheet" href="https://fonts.googleapis.com/css2?family=Open+Sans:wght@400;600;700&display=swap">
<style>
  :root {
    --stage-bg: #e9e6e2;
    --card-bg: #ffffff;
    --brand-red: #e1232b;
    --ink: #1d1d1d;
    --rule: #111111;
    --faint: #f1f1f1;
  }
  * { margin: 0; padding: 0; box-sizing: border-box; }
  html, body { width: 1200px; height: 1000px; overflow: hidden; }
  body {
    background: var(--stage-bg);
    font-family: "Open Sans", Arial, sans-serif;
    color: var(--ink);
    position: relative;
  }
  .card {
    position: absolute;
    left: 265px;
    width: 665px;
    height: 397px;
    background: var(--card-bg);
    border-radius: 22px;
    box-shadow: 0 4px 14px rgba(0,0,0,0.18);
    overflow: hidden;
  }
  .card--front { top: 73px; }
  .card--back { top: 533px; }

  .backdrop-mark {
    position: absolute;
    border-radius: 50%;
    background: var(--faint);
  }
  .card--front .backdrop-mark { left: 380px; top: 150px; width: 230px; height: 230px; }
  .card--back .backdrop-mark { left: 170px; top: 140px; width: 230px; height: 230px; }

  .brand {
    position: absolute;
    display: flex;
    align-items: center;
    gap: 12px;
  }
  .card--front .brand { right: 36px; top: 66px; }
  .card--back .brand { left: 160px; top: 62px; }
  .brand-dot {
    width: 34px; height: 34px;
    border-radius: 50%;
    background: var(--brand-red);
    flex: none;
  }
  .brand-name {
    font-weight: 600;
    font-size: 29px;
    color: var(--ink);
    letter-spacing: 0.2px;
    white-space: nowrap;
  }

  .contact {
    position: absolute;
    left: 33px;
    top: 155px;
  }
  .person-name {
    color: var(--brand-red);
    font-weight: 600;
    font-size: 22px;
    line-height: 30px;
  }
  .person-role {
    font-size: 16px;
    line-height: 22px;
  }
  .contact-list {
    list-style: none;
    margin-top: 14px;
  }
  .contact-list li {
    display: flex;
    align-items: center;
    gap: 7px;
    font-size: 16px;
    line-height: 23.5px;
  }
  .contact-list svg { width: 14px; height: 14px; flex: none; fill: var(--brand-red); }
  .address {
    margin-top: 12px;
    font-size: 16px;
    line-height: 22px;
  }

  .writing-lines {
    position: absolute;
    left: 32px;
    top: 197px;
    width: 602px;
    list-style: none;
  }
  .writing-lines li {
    height: 2px;
    background: var(--rule);
    margin-bottom: 46px;
  }
</style>
</head>
<body>

<section class="card card--front" aria-label="Card front">
  <div class="backdrop-mark" aria-hidden="true"></div>
  <div class="brand">
    <span class="brand-dot" aria-hidden="true"></span>
    <span class="brand-name">Bayline Mosquito Care</span>
  </div>
  <div class="contact">
    <p class="person-name">Dana Corvell</p>
    <p class="person-role">Director of operations</p>
    <ul class="contact-list">
      <li>
        <svg viewBox="0 0 14 14" aria-hidden="true"><rect x="3.5" y="0.5" width="7" height="13" rx="1.2"/><rect x="5" y="2.5" width="4" height="4" fill="#fff"/></svg>
        + 000 000 0000
      </li>
      <li>
        <svg viewBox="0 0 14 14" aria-hidden="true"><path d="M1 5c0-2 2-3 6-3s6 1 6 3v1h-3V4.5H4V6H1z"/><path d="M3 7h8l1.5 5h-11z"/></svg>
        + 000 000 0000
      </li>
      <li>
        <svg viewBox="0 0 14 14" aria-hidden="true"><rect x="1" y="3" width="12" height="8.5"/><path d="M1.5 3.5 7 8l5.5-4.5" stroke="#fff" stroke-width="1.2" fill="none"/></svg>
        hello@baylinemozzie.com
      </li>
      <li>
        <svg viewBox="0 0 14 14" aria-hidden="true"><circle cx="7" cy="7" r="6"/><path d="M1 7h12M7 1c-2.5 3-2.5 9 0 12M7 1c2.5 3 2.5 9 0 12" stroke="#fff" stroke-width="1" fill="none"/></svg>
        www.baylinemozzie.com
      </li>
    </ul>
    <p class="address">Level 4, 18 Harbour Lane<br>Brisbane, 40, Queensland</p>
  </div>
</section>

<section class="card card--back" aria-label="Card back">
  <div class="backdrop-mark" aria-hidden="true"></div>
  <div class="brand">
    <span class="brand-dot" aria-hidden="true"></span>
    <span class="brand-name">Bayline Mosquito Care</span>
  </div>
  <ul class="writing-lines" aria-label="Lines for handwritten notes">
    <li></li><li></li><li></li><li></li>
  </ul>
</section>

</body>
</html>
```